Book Cover

Hello!
I need someone to design a book cover with the title, subtitle and one of the photos attached.

- Title: Beyond the Grey Hours - By Corwin Ashdale
- Subtitle: A Steady Handbook for finding calm and strength after hard news.

```html
<!DOCTYPE html>
<html lang="en">
<head>
<meta charset="utf-8">
<title>Beyond the Grey Hours — Book Cover</title>
<link href="https://fonts.googleapis.com/css2?family=Roboto:wght@400;700;900&family=Poppins:wght@600;700&display=swap" rel="stylesheet">
<style>
  :root {
    --page-bg: #f1f1ef;
    --navy: #1f3679;
    --navy-mid: #4e6599;
    --pale: #e0eef5;
    --title-grey: #c8d5de;
    --body-white: #ffffff;
    --accent-orange: #f0a830;
    --spine-light: #bde0fa;
    --front-title: #2a2e0a;
    --front-sub: #1e2f6b;
    --sky-top: #9cc7ec;
    --sky-mid: #c5def3;
    --coat-blue: #2a4f9e;
  }
  * { margin: 0; padding: 0; box-sizing: border-box; }
  html, body { width: 1200px; height: 783px; overflow: hidden; background: var(--page-bg); }
  .canvas { position: relative; width: 1200px; height: 783px; }

  /* Back cover */
  .back-cover {
    position: absolute; left: 50px; top: 6px; width: 503px; height: 758px;
    background: linear-gradient(180deg, var(--navy) 0%, var(--navy) 14%, var(--navy-mid) 40%, #a9bcd4 72%, var(--pale) 100%);
    box-shadow: -2px 2px 4px rgba(0,0,0,.25);
    font-family: "Poppins", sans-serif; font-weight: 600; color: var(--body-white);
    text-transform: uppercase;
  }
  .back-title {
    position: absolute; left: 0; right: 0; top: 44px; text-align: center;
    font-family: "Roboto", sans-serif; font-size: 28px; font-weight: 400; color: var(--title-grey);
    letter-spacing: .2px;
  }
  .back-title strong { font-weight: 900; }
  .blurb-lead {
    position: absolute; left: 50px; width: 405px; top: 112px;
    font-size: 9px; line-height: 13px; text-align: center;
  }
  .blurb {
    position: absolute; left: 44px; width: 418px;
    font-size: 9.6px; line-height: 16.2px; text-align: justify; text-align-last: left;
  }
  .blurb.p1 { top: 197px; }
  .blurb.p2 { top: 326px; }
  .blurb.p3 { top: 423px; }
  .author-photo {
    position: absolute; left: 41px; top: 507px; width: 85px; height: 120px;
    border: 2px solid var(--accent-orange);
    background: linear-gradient(180deg, #cfe0ea 0%, #b9a77b 35%, #3a5aa0 60%, #1e3473 100%);
  }
  .author-bio {
    position: absolute; left: 133px; top: 524px; width: 338px;
    font-size: 9.6px; line-height: 16.2px; text-align: justify; text-align-last: left;
  }
  .author-bio .name { font-family: "Poppins", sans-serif; font-weight: 700; font-size: 11.5px; color: var(--title-grey); }
  .code-box {
    position: absolute; left: 316px; top: 637px; width: 170px; height: 100px;
    background: #fffdf6; border: 2px solid var(--accent-orange);
  }

  /* Spine */
  .spine { position: absolute; left: 571px; top: 6px; width: 64px; height: 758px; }
  .spine-top { position: absolute; left: 0; top: 0; width: 64px; height: 523px; background: linear-gradient(180deg, var(--navy) 0%, #5a74ac 100%); }
  .spine-bottom { position: absolute; left: 0; top: 523px; width: 64px; height: 235px; background: var(--spine-light); }
  .spine-title, .spine-author {
    position: absolute; writing-mode: vertical-rl; font-family: "Roboto", sans-serif; font-weight: 900;
    white-space: nowrap;
  }
  .spine-title { left: 14px; top: 52px; font-size: 31px; color: #fff; letter-spacing: .3px; }
  .spine-author { left: 20px; top: 545px; font-size: 20px; color: #000; letter-spacing: .5px; }

  /* Front cover */
  .front-cover { position: absolute; left: 652px; top: 4px; width: 504px; height: 760px; overflow: hidden; }
  .cover-photo {
    position: absolute; inset: 0;
    background:
      radial-gradient(ellipse 55% 60% at 55% 95%, var(--coat-blue) 0%, rgba(42,79,158,.85) 55%, rgba(42,79,158,0) 75%),
      linear-gradient(180deg, var(--sky-top) 0%, var(--sky-mid) 45%, #cfd8dc 100%);
  }
  .front-text { position: absolute; right: 12px; top: 76px; text-align: right; font-family: "Roboto", sans-serif; }
  .front-title { color: var(--front-title); line-height: 1; }
  .front-title .t1 { display: block; font-size: 35px; font-weight: 700; letter-spacing: .5px; }
  .front-title .t2 { display: block; font-size: 38px; font-weight: 900; margin-top: 4px; }
  .front-subtitle {
    margin-top: 12px; width: 350px; margin-left: auto;
    font-size: 14px; font-weight: 900; line-height: 16px; color: var(--front-sub); text-transform: uppercase;
  }
  .front-author { margin-top: 18px; font-size: 20px; font-weight: 900; color: var(--front-title); letter-spacing: 1px; }
</style>
</head>
<body>
<main class="canvas">
  <section class="back-cover">
    <h2 class="back-title">BEYOND THE <strong>GREY HOURS</strong></h2>
    <p class="blurb-lead">Lorem ipsum dolor sit amet, consectetuer adipiscing elit. Aenean commodo ligula eget dolor. Aenean massa. Cum sociis natoque penatibus et magnis dis parturient montes, nascetur ridiculus mus. Donec quam felis, ultricies nec, pellentesque eu, pretium quis, sem. Nulla consequat massa quis enim. Donec pede justo, fringilla vel, aliquet nec,</p>
    <p class="blurb p1">Vulputate eget, arcu. In enim justo, rhoncus ut, imperdiet a, venenatis vitae, justo. Nullam dictum felis eu pede mollis pretium. Integer tincidunt. Cras dapibus. Vivamus elementum semper nisi. Aenean vulputate eleifend tellus. Aenean leo ligula, porttitor eu, consequat vitae, eleifend ac, enim. Aliquam lorem ante, dapibus in, viverra quis, feugiat a, tellus. Phasellus viverra nulla ut metus varius laoreet. Quisque rutrum. Aenean</p>
    <p class="blurb p2">Imperdiet. Etiam ultricies nisi vel augue. Curabitur ullamcorper ultricies nisi. Nam eget dui. Etiam rhoncus. Maecenas tempus, tellus eget condimentum rhoncus, sem quam semper libero, sit amet adipiscing sem neque sed ipsum. Nam quam nunc, blandit vel, luctus pulvinar, hendrerit id, lorem. Maecenas nec odio et ante tincidunt tempus. Donec</p>
    <p class="blurb p3">Vitae sapien ut libero venenatis faucibus. Nullam quis ante. Etiam sit amet orci eget eros faucibus tincidunt. Duis leo. Sed fringilla mauris sit amet nibh. Donec sodales sagittis magna. Sed consequat, leo eget bibendum sodales, augue velit cursus nunc,</p>
    <div class="author-photo" role="img" aria-label="Portrait of the author standing in a meadow in a blue jacket"></div>
    <p class="author-bio"><span class="name">Corwin Ashdale</span> Vitae sapien ut libero venenatis faucibus. Nullam quis ante. Etiam sit amet orci eget eros faucibus tincidunt. Duis leo. Sed fringilla mauris sit amet nibh. Donec sodales sagittis magna. Sed consequat, leo eget bibendum sodales, augue velit cursus nunc,</p>
    <div class="code-box"></div>
  </section>

  <section class="spine">
    <div class="spine-top"></div>
    <div class="spine-bottom"></div>
    <span class="spine-title">BEYOND THE GREY HOURS</span>
    <span class="spine-author">CORWIN ASHDALE</span>
  </section>

  <section class="front-cover">
    <div class="cover-photo" role="img" aria-label="Photo of the author outdoors under bare trees and a blue sky, wearing a blue jacket and looking upward"></div>
    <div class="front-text">
      <h1 class="front-title"><span class="t1">BEYOND THE</span><span class="t2">GREY HOURS</span></h1>
      <p class="front-subtitle">A Steady Handbook for finding calm and strength after hard news.</p>
      <p class="front-author">BY CORWIN ASHDALE</p>
    </div>
  </section>
</main>
</body>
</html>
```